Executive Education Business needs a brochure for an IT Security workshop

UPDATE AND CLARIFICATION - I'm looking for a brochure that includes the text from the attached file "2014 IT Security Program Outline v2". This is a specific program we are putting on that we need a brochure designed for, using the content included in this file.

We have the basic text of a brochure, and need a design layout for a brochure that we can use to market this workshop to financial institutions in Asia and the Middle East. It may make sense to leave a spot on the cover somewhere to add a location and date (which we can edit based on program scheduling). Additionally, a registration page should be included either in the brochure or as an insert.

I'm attaching a brochure we used for a past program which provides an example registration page for our programs. I'm also including some photos from our programs that may be of use, although stock photography is also acceptable. Finally, I'm including two of our corporate brochures that may provide additional background on the company and our style.

```html
<!DOCTYPE html>
<html lang="en">
<head>
<meta charset="utf-8">
<title>IT Security Program – Brochure and Registration Form</title>
<link href="https://fonts.googleapis.com/css2?family=Source+Sans+3:wght@300;400;600;700&display=swap" rel="stylesheet">
<style>
  :root {
    --backdrop: #3a3a3a;
    --paper: #ffffff;
    --panel-gray-start: #f4f4f4;
    --panel-gray-end: #cfcfcf;
    --ink: #2a2a2a;
    --ink-soft: #555555;
    --ink-light: #8a8a8a;
    --rule: #9a9a9a;
    --divider: #c8c8c8;
    --photo-tone: #9d9d9d;
  }
  * { box-sizing: border-box; margin: 0; padding: 0; }
  html, body { width: 1200px; height: 793px; overflow: hidden; }
  body {
    background: var(--backdrop);
    font-family: "Source Sans 3", sans-serif;
    color: var(--ink);
    position: relative;
  }

  /* Brochure spread */
  .brochure-spread {
    position: absolute;
    left: 24px; top: 40px;
    width: 680px; height: 470px;
    display: grid;
    grid-template-columns: 300px 380px;
    background: var(--paper);
  }
  .speakers-panel {
    display: grid;
    grid-template-columns: 1fr 1fr;
    gap: 14px;
    padding: 22px 14px 22px 18px;
  }
  .speaker { font-size: 8.6px; line-height: 1.32; color: var(--ink-soft); }
  .speaker + .speaker { border-left: 1px solid var(--divider); padding-left: 12px; }
  .speaker-photo {
    width: 70px; height: 70px; border-radius: 50%;
    background: radial-gradient(circle at 50% 40%, #c4c4c4, var(--photo-tone));
    margin: 0 auto 20px;
  }
  .speaker-name {
    font-size: 13px; font-weight: 700; color: var(--ink);
    margin-bottom: 2px; line-height: 1.1;
  }
  .sessions-panel {
    display: grid;
    grid-template-columns: 1fr 1fr;
    gap: 16px;
    padding: 14px 16px;
    background: linear-gradient(90deg, var(--panel-gray-end), var(--panel-gray-start) 18%, var(--panel-gray-start));
    font-size: 8.4px; line-height: 1.33; color: var(--ink-soft);
  }
  .session-label { font-size: 12px; font-weight: 700; color: var(--ink); margin-top: 8px; }
  .session-title { font-size: 10.5px; font-weight: 300; color: var(--ink); margin-bottom: 2px; }
  .session p { margin-bottom: 4px; }

  /* Registration form */
  .registration-form {
    position: absolute;
    left: 760px; top: 120px;
    width: 357px; height: 552px;
    background: var(--paper);
    padding: 38px 30px 20px 32px;
    display: flex; flex-direction: column;
  }
  .form-header { display: flex; justify-content: space-between; align-items: flex-start; }
  .form-heading { font-size: 18px; font-weight: 400; letter-spacing: 0.2px; margin-top: 2px; }
  .brand-mark { display: flex; align-items: center; gap: 5px; color: var(--ink-light); font-size: 9px; font-weight: 600; margin-top: -14px; }
  .brand-dot { width: 12px; height: 12px; border-radius: 50%; background: var(--ink-light); }
  .program-title { font-size: 9.5px; color: var(--ink-soft); margin-top: 42px; }
  .program-when-where { font-size: 10px; color: var(--ink-soft); margin-top: 32px; line-height: 1.3; }
  .form-fields { list-style: none; margin-top: 40px; }
  .form-field {
    font-size: 8.2px; color: var(--ink-soft);
    height: 22.2px; padding-top: 8px;
    border-bottom: 1px dashed var(--rule);
    margin-right: 2px;
  }
  .form-notes { margin-top: auto; font-size: 6.4px; color: var(--ink-soft); line-height: 1.35; padding-bottom: 10px; }
  .form-notes p + p { margin-top: 6px; }
</style>
</head>
<body>

<section class="brochure-spread">
  <div class="speakers-panel">
    <article class="speaker">
      <div class="speaker-photo" role="img" aria-label="Portrait photo of speaker Marc Delaunier"></div>
      <h3 class="speaker-name">Marc Delaunier</h3>
      <p>knows how banks work from the inside. He has run the operations and information technology of banks including Harlow Partners, Westbridge Capital and most recently was the Chief Operating Officer of Gulfstone Commercial Bank. His experience in running middle and back office operations and IT, often involving complex derivative products, gives him a practical understanding of operational risk management. He is a French National and graduated from the Lormont School of Commerce. He is a qualified "Expert Comptable Mémorialiste" (French ACA) and began his career as an auditor with Carver and Lyle.</p>
    </article>
    <article class="speaker">
      <div class="speaker-photo" role="img" aria-label="Portrait photo of speaker Layla Haddad"></div>
      <h3 class="speaker-name">Layla Haddad</h3>
      <p>is an independent Information Security consultant and has co-authored several articles and patents in the fields of embedded security, cryptography, intrusion detection, cyber physical systems, and Operating Systems security. She is also a Senior Associate at Brandt &amp; Company, serving large corporate clients in the information and communications technology industry, with a focus on information security and risk management, information governance, corporate strategy, and corporate governance. She holds a Ph.D. in Information Security from Easton University, and has served clients in the USA, the Middle East, Australia, Africa, and Asia.</p>
    </article>
  </div>

  <div class="sessions-panel">
    <div>
      <section class="session">
        <h4 class="session-label">Session 2</h4>
        <h5 class="session-title">Information Governance</h5>
        <p>In the course of their operations, organizations in all sectors create, process, and use sensitive information and are in need of protection. Information Security is therefore a major concern to any organization, serving to protect its information assets, mitigate security attacks, ensure competitiveness, and maintain brand image and equity.</p>
        <p>This session addresses the need of organizations to build assets and information inventories, classify such inventories, and build a framework of security controls and policies across all levels of an organization based on exposure to vulnerability exploits, cyber threats, and associated risks.</p>
      </section>
      <section class="session">
        <h4 class="session-label">Session 3</h4>
        <h5 class="session-title">Embedded Systems and Security</h5>
        <p>Embedded systems are ubiquitously used to capture, store, and manipulate data of a sensitive nature (e.g., consumer appliances such as cell phones, tablets, smart cards, personal computers, wireless handsets, networked sensors, etc.), and to perform critical functions (e.g., automotive and avionics systems, medical appliances, etc.). As these systems become more complex and connected, with the ability to receive and download programs from public networks, their security is a serious concern in their design.</p>
      </section>
    </div>
    <div>
      <section class="session">
        <h4 class="session-label">Session 4</h4>
        <h5 class="session-title">People and Operational Risk</h5>
        <p>Unfortunately, people are often the weakest link in a security chain. In this session we address the personal side of security and how technical solutions can be put at risk if an organization does not have the appropriate risk culture or adequate risk awareness. We will identify key areas of "people risk" and describe best practices for system design that take these human factors into account.</p>
        <p>Additionally, we will discuss various IT operational risks, business continuity planning, and disaster recovery. In particular, we will focus on the roles and responsibilities required in managing these risks and will outline practical lessons for Board members, senior management, and IT professionals in working together to minimize the impact of operational risks.</p>
      </section>
    </div>
  </div>
</section>

<section class="registration-form">
  <header class="form-header">
    <h1 class="form-heading">REGISTRATION FORM</h1>
    <div class="brand-mark"><span class="brand-dot"></span>meridianexec.com</div>
  </header>
  <p class="program-title">IT Security: Protecting the Integrity of your Technology Platforms</p>
  <p class="program-when-where">Date: XX.XX, 2014<br>Venue: Harbour Crest Hotel, Manama, Bahrain</p>
  <ul class="form-fields">
    <li class="form-field">Name</li>
    <li class="form-field">Company</li>
    <li class="form-field">Title</li>
    <li class="form-field">Contact Number</li>
    <li class="form-field">Fax Number</li>
    <li class="form-field">Email</li>
    <li class="form-field">Professional certification and education</li>
    <li class="form-field">Name and title of direct supervisor</li>
    <li class="form-field">Secretary Name</li>
    <li class="form-field">Secretary Contact Number</li>
    <li class="form-field">Secretary Email</li>
  </ul>
  <footer class="form-notes">
    <p>Completed forms may be faxed to +1-555-010-4000 or emailed to info@meridianexec.com.</p>
    <p>Payment should be made within 30 days upon receipt of invoice to secure a place in the program, and must be made prior to the start of the program.</p>
  </footer>
</section>

</body>
</html>
```